Corvale Enterprises -Business Card Design Project

I have a new logo to put onto business cards - attached
The word doc shows how I want it all laid out - front page and rear
The lettering I want is clean and rounded - modern
Reason: There was no original deadline!
Target Market(s)
25-49 year old leaders and entrepreneurs in Australia
Industry/Entity Type
Business

```html
<!DOCTYPE html>
<html lang="en">
<head>
<meta charset="utf-8">
<title>Corvale Enterprises – Business Card</title>
<link href="https://fonts.googleapis.com/css2?family=Montserrat:wght@500;700&family=Questrial&display=swap" rel="stylesheet">
<style>
  :root {
    --stage: #f1f1f1;
    --ink-dark: #232323;
    --paper: #ffffff;
    --brand-blue: #1448b0;
    --mid-grey: #8d8d8d;
    --soft-grey: #5a5a5a;
    --text-dark: #222222;
    --text-light: #ffffff;
  }
  * { box-sizing: border-box; margin: 0; padding: 0; }
  html, body { width: 1200px; height: 720px; overflow: hidden; }
  body {
    background: var(--stage);
    font-family: "Questrial", "Century Gothic", sans-serif;
    position: relative;
  }
  .card {
    position: absolute;
    width: 520px;
    height: 300px;
    top: 210px;
    box-shadow: 0 2px 6px rgba(0,0,0,.12);
    overflow: hidden;
  }

  /* ---------- front ---------- */
  .card--front { left: 50px; background: var(--paper); }
  .front__panel {
    position: absolute; left: 0; top: 0; bottom: 0; width: 200px;
    background: var(--ink-dark);
  }
  .front__services {
    position: absolute; left: 24px; bottom: 28px;
    list-style: none; color: var(--text-light);
    font-family: "Montserrat", sans-serif; font-weight: 700;
    font-size: 12px; line-height: 1.55;
  }
  .front__body { position: absolute; left: 228px; top: 30px; right: 20px; }
  .brand-name {
    font-family: "Montserrat", sans-serif; font-weight: 700;
    color: var(--brand-blue); line-height: 1.1;
  }
  .front__body .brand-name { font-size: 24px; }
  .tagline { font-size: 8px; letter-spacing: 0.8px; color: var(--mid-grey); margin-top: 6px; }
  .front__slogan { font-size: 12px; color: var(--text-dark); margin-top: 14px; line-height: 1.35; }
  .person { margin-top: 16px; }
  .person__name { font-size: 19px; color: var(--brand-blue); }
  .person__role { font-family: "Montserrat", sans-serif; font-weight: 700; font-size: 12px; color: var(--text-dark); }
  .contact { list-style: none; margin-top: 10px; font-size: 12px; color: var(--text-dark); line-height: 1.6; }
  .contact li { display: flex; align-items: center; gap: 6px; }
  .contact svg { width: 11px; height: 11px; flex: none; }

  /* ---------- back ---------- */
  .card--back { left: 630px; background: var(--ink-dark); }
  .back__lockup { position: absolute; left: 30px; right: 30px; top: 96px; text-align: center; }
  .back__lockup .brand-name { font-size: 40px; }
  .back__lockup .tagline { font-size: 11px; letter-spacing: 1.6px; color: var(--soft-grey); margin-top: 14px; }
  .back__web {
    position: absolute; left: 0; right: 0; bottom: 42px; text-align: center;
    font-family: "Montserrat", sans-serif; font-weight: 700; font-size: 13px; color: var(--soft-grey);
  }
</style>
</head>
<body>

<section class="card card--front">
  <div class="front__panel">
    <ul class="front__services">
      <li>NLP Practitioner &amp; Coach</li>
      <li>Personal, Business &amp; Staff</li>
      <li>Development</li>
      <li>Self Resilience Programs</li>
    </ul>
  </div>

  <div class="front__body">
    <h1 class="brand-name">Corvale Enterprises</h1>
    <p class="tagline">Mind Training | Coaching | Business Development</p>
    <p class="front__slogan">Direction and Growth<br>For Leaders and Entrepreneurs</p>

    <div class="person">
      <p class="person__name">Declan Hartley</p>
      <p class="person__role">Director</p>
    </div>

    <ul class="contact">
      <li>ABN: 47 302 918 564</li>
      <li>
        <svg viewBox="0 0 12 12" aria-hidden="true"><rect x="3" y="0.5" width="6" height="11" rx="1.2" fill="var(--brand-blue)"/><rect x="4" y="2" width="4" height="6" fill="#fff"/></svg>
        0431 276 518
      </li>
      <li>
        <svg viewBox="0 0 12 12" aria-hidden="true"><rect x="0.5" y="2.5" width="11" height="7" fill="none" stroke="var(--brand-blue)"/><path d="M0.5 2.5 L6 7 L11.5 2.5" fill="none" stroke="var(--brand-blue)"/></svg>
        declan@corvaleenterprises.com.au
      </li>
    </ul>
  </div>
</section>

<section class="card card--back">
  <div class="back__lockup">
    <h2 class="brand-name">Corvale Enterprises</h2>
    <p class="tagline">Mind Training | Coaching | Business Development</p>
  </div>
  <p class="back__web">corvaleenterprises.com.au</p>
</section>

</body>
</html>
```